Barrister at Law needs Business Card Design

Need a business card design for Barrister at Law. Double sided. Simple Tom Wexley and Barrister at Law on one side with contact details on the other side. I would like a professional design using Black or Platinum. Details on reverse side would include qualifications - Bcom-Llb and Acc Spec Commercial Litigation. I have attached the logo. Contact details would include address/ Po Box/ Phone/Fax/Mobile/email. I would like to use raised print or spot gloss.

```html
<!DOCTYPE html>
<html lang="en">
<head>
<meta charset="utf-8">
<title>Tom Wexley – Barrister-at-Law Business Card</title>
<link rel="stylesheet" href="https://fonts.googleapis.com/css2?family=Cinzel:wght@400;500&family=Open+Sans:wght@400;600&display=swap">
<style>
  :root {
    --backdrop: #3a3431;
    --card-black: #141414;
    --card-edge: #0a0a0a;
    --silver-light: #f2f2f2;
    --silver-mid: #bdbdbd;
    --silver-dark: #6e6e6e;
    --text-light: #e8e8e8;
    --text-dark: #1a1a1a;
    --accent-blue: #1f7fc4;
  }
  * { margin: 0; padding: 0; box-sizing: border-box; }
  html, body { width: 1200px; height: 814px; overflow: hidden; background: var(--backdrop); }
  .canvas { position: relative; width: 1200px; height: 814px; }

  .card {
    position: absolute;
    width: 520px;
    height: 300px;
    background: var(--card-black);
    border-radius: 4px;
    box-shadow: 0 10px 28px rgba(0,0,0,.45);
    overflow: hidden;
  }
  .card--front { left: 50px; top: 257px; }
  .card--back { left: 630px; top: 257px; }

  .front-name {
    position: absolute;
    left: 78px; top: 92px;
    font-family: "Cinzel", serif;
    font-weight: 500;
    font-size: 36px;
    letter-spacing: 1px;
    background: linear-gradient(180deg, var(--silver-light) 0%, var(--silver-mid) 55%, var(--silver-dark) 100%);
    -webkit-background-clip: text;
    background-clip: text;
    color: transparent;
  }
  .front-title {
    position: absolute;
    left: 80px; top: 142px;
    font-family: "Cinzel", serif;
    font-size: 19px;
    letter-spacing: 1px;
    color: var(--silver-mid);
  }

  .brand-name {
    position: absolute;
    left: 36px; top: 36px;
    font-family: "Open Sans", sans-serif;
    font-weight: 600;
    font-size: 20px;
    color: var(--text-light);
    display: flex; align-items: center; gap: 10px;
  }
  .brand-mark { width: 14px; height: 14px; background: var(--accent-blue); }

  .contact-list {
    position: absolute;
    right: 26px; top: 118px;
    list-style: none;
    font-family: "Open Sans", sans-serif;
    font-size: 13px;
    line-height: 20px;
    color: var(--text-light);
    text-align: right;
  }
  .contact-list li { display: flex; justify-content: flex-end; align-items: center; gap: 8px; }
  .contact-icon { width: 12px; height: 12px; display: inline-block; }
  .contact-icon--blank { width: 12px; }

  .silver-band { position: absolute; left: 0; bottom: 0; width: 520px; height: 80px; }
  .web-address {
    position: absolute;
    right: 26px; bottom: 12px;
    font-family: "Open Sans", sans-serif;
    font-size: 15px;
    letter-spacing: 3px;
    color: var(--text-dark);
  }
</style>
</head>
<body>
<main class="canvas">
  <section class="card card--front" aria-label="Card front">
    <h1 class="front-name">Tom Wexley</h1>
    <p class="front-title">Barrister-at-Law</p>
  </section>

  <section class="card card--back" aria-label="Card back">
    <div class="brand-name"><span class="brand-mark"></span>Wexley Law</div>

    <ul class="contact-list">
      <li>218 Cedar Ridge Lane<span class="contact-icon contact-icon--blank"></span></li>
      <li>Fairbanks, Alaska 99701<span class="contact-icon contact-icon--blank"></span></li>
      <li>555 201 4830<span class="contact-icon contact-icon--blank"></span></li>
      <li>555 318 7726
        <svg class="contact-icon" viewBox="0 0 12 12"><path d="M3 1c1 0 1.6 2 1.6 2.6 0 .6-.8.9-.8 1.3.3 1.2 1.6 2.5 2.8 2.8.4 0 .7-.8 1.3-.8S11 8 11 9s-1 2-2 2C5.2 11 1 6.8 1 3c0-1 1-2 2-2z" fill="var(--accent-blue)"/></svg>
      </li>
      <li>555 464 1095
        <svg class="contact-icon" viewBox="0 0 12 12"><rect x="3" y="0.5" width="6" height="11" rx="1" fill="none" stroke="var(--accent-blue)" stroke-width="1.2"/><circle cx="6" cy="9.6" r=".7" fill="var(--accent-blue)"/></svg>
      </li>
      <li>tom@wexleylaw.com
        <svg class="contact-icon" viewBox="0 0 12 12"><rect x="0.5" y="2.5" width="11" height="7" fill="var(--accent-blue)"/><path d="M.5 2.5 6 6.5l5.5-4" fill="none" stroke="var(--card-black)" stroke-width="1"/></svg>
      </li>
    </ul>

    <svg class="silver-band" viewBox="0 0 520 80" aria-hidden="true">
      <defs>
        <linearGradient id="silverSweep" x1="0" y1="0" x2="1" y2="0">
          <stop offset="0" stop-color="#f4f4f4"/>
          <stop offset=".35" stop-color="#9a9a9a"/>
          <stop offset=".6" stop-color="#3a3a3a"/>
          <stop offset="1" stop-color="#1a1a1a"/>
        </linearGradient>
      </defs>
      <path d="M0 8 L260 24 L520 40 L520 80 L0 80 Z" fill="url(#silverSweep)"/>
      <path d="M0 30 L240 42 L262 34 L520 48 L520 80 L0 80 Z" fill="#ffffff"/>
      <path d="M0 30 L240 42 L262 34 L520 48" fill="none" stroke="#8a8a8a" stroke-width="1"/>
    </svg>
    <p class="web-address">www.wexleylaw.com</p>
  </section>
</main>
</body>
</html>
```